One page informative flyer for Florist

We are looking for a simple one page flyer. We are a florist who sell flowers, and commemorative t-shirts at graduation ceremonies, and need a flyer that can be given out to students so that they will know what is available on site. Further, we want the flyer to be editable (ie. a word template, or some other program), so that we can change the schools name, and change small bits of the copy easily.

What we are really looking for is a simple template, but we need 4 iterations of the flyer. With each of our two logos, I will need a flyer for t-shirts, and a flyer for flowers. Making 4 total. Please see breakdown below as explanation:

1, Tassel Lane Flowers logo - flyer for flowers
2. Tassel Lane Flowers logo - flyer for shirts
3. Gownbright Flowers logo - flyer for flowers
4. Gownbright Flowers logo - flyer for shirts

Please see logos for Tassel Lane Flowers and Gownbright Flowers attached, as well as a picture of flowers and of the shirts. Feel free to use those images or stock images.

Here is the copy:

Flowers - A variety floral arrangements will be available for purchase at our stand, located conveniently at the graduation ceremony. You can browse our selection & pre-order ahead of time at: www.gownbrightflowers.example/index,php/test

T-Shirts - Commerative T-Shirts displaying all of the students names will be available for purchase at our stand, located conveniently at the graduation ceremony. You can pre-order ahead of time to guarantee your choice of size at: www.gownbrightflowers.example/index.php/test

```html
<!DOCTYPE html>
<html lang="en">
<head>
<meta charset="utf-8">
<title>Gownbright Flowers – Flowers Flyer</title>
<link href="https://fonts.googleapis.com/css2?family=Oswald:wght@500&family=Great+Vibes&family=Tinos&display=swap" rel="stylesheet">
<style>
  :root {
    --backdrop: #1f1f1f;
    --paper: #ffffff;
    --blush: #f9e9f0;
    --leaf: #7aa040;
    --leaf-light: #9cc45a;
    --ink: #111111;
    --rose-deep: #d98aa6;
    --rose-soft: #f6d3df;
    --petal-white: #fbf3f6;
    --foliage: #8fb26a;
  }
  * { margin: 0; padding: 0; box-sizing: border-box; }
  html, body {
    width: 1200px; height: 999px; overflow: hidden;
    background: var(--backdrop);
  }
  .flyer {
    position: absolute; left: 262px; top: 20px;
    width: 676px; height: 957px;
    background: var(--paper);
    overflow: hidden;
  }
  .flyer-shapes { position: absolute; inset: 0; }
  .brand-name {
    position: absolute; right: 178px; top: 436px;
    font-family: "Oswald", "Arial Narrow", sans-serif;
    font-weight: 500; font-size: 56px; line-height: 58px;
    color: var(--leaf); text-align: right; letter-spacing: -0.5px;
  }
  .section-title {
    position: absolute; left: 20px; top: 618px;
    font-family: "Great Vibes", cursive;
    font-size: 100px; line-height: 1;
    color: var(--leaf-light);
  }
  .info-copy {
    position: absolute; left: 0; top: 772px; width: 676px;
    padding: 0 24px;
    font-family: "Tinos", "Times New Roman", serif;
    font-size: 25px; line-height: 32.5px;
    color: var(--ink); text-align: center;
  }
  .info-copy .site-link { display: block; padding-left: 24px; }
</style>
</head>
<body>
  <main class="flyer">
    <svg class="flyer-shapes" viewBox="0 0 676 957" width="676" height="957" aria-hidden="false">
      <defs>
        <linearGradient id="roseBouquet" x1="0" y1="0" x2="0" y2="1">
          <stop offset="0" stop-color="#fdfafb"/>
          <stop offset="0.2" stop-color="var(--rose-deep)"/>
          <stop offset="0.6" stop-color="#e9a9bf"/>
          <stop offset="1" stop-color="var(--petal-white)"/>
        </linearGradient>
        <linearGradient id="mixedBouquet" x1="0" y1="0" x2="1" y2="1">
          <stop offset="0" stop-color="var(--petal-white)"/>
          <stop offset="0.45" stop-color="var(--rose-soft)"/>
          <stop offset="0.75" stop-color="#f2f0f0"/>
          <stop offset="1" stop-color="var(--foliage)"/>
        </linearGradient>
      </defs>

      <!-- blush banding -->
      <rect class="blush-band" x="0" y="400" width="676" height="150" fill="var(--blush)"/>
      <rect class="copy-panel" x="0" y="772" width="676" height="170" fill="var(--blush)"/>

      <!-- hero photo area -->
      <polygon class="hero-photo" role="img" aria-label="Photo of a bouquet of pink roses lying on a white surface with scattered petals"
        points="0,0 676,0 676,352 548,352 522,420 0,420" fill="url(#roseBouquet)"/>
      <polygon class="blush-corner" points="548,352 676,352 676,420 522,420" fill="var(--blush)"/>

      <!-- green accent band -->
      <polygon class="leaf-band" points="0,437 130,437 222,565 0,565" fill="var(--leaf)"/>
      <polyline class="leaf-rule" points="224,566 645,566 676,612" fill="none" stroke="var(--leaf)" stroke-width="3"/>

      <!-- lower photo area -->
      <polygon class="bouquet-photo" role="img" aria-label="Photo of an arrangement of pink roses and white alstroemeria lilies with green leaves"
        points="226,569 644,569 676,617 676,772 292,772" fill="url(#mixedBouquet)"/>

      <!-- footer bar -->
      <rect class="footer-bar" x="0" y="942" width="676" height="15" fill="var(--leaf)"/>
    </svg>

    <h1 class="brand-name">Gownbright<br>Flowers</h1>
    <h2 class="section-title">Flowers</h2>
    <p class="info-copy">
      A variety floral arrangements will be available for purchase at our stand, located conveniently at the graduation ceremony. You can browse our selection &amp; pre-order ahead of time at:
      <span class="site-link">www.gownbrightflowers.example/index,php/test</span>
    </p>
  </main>
</body>
</html>
```